New flavour! New packaging for Velocity Energy Drink!

We need a new packaging designed to show off our new grape flavored energy drink! It will require box design with matching sachets!

Established in 2018 we are a fully Australian owned and operated business that started out with 2 gamers that got sick and tired of sugary energy drinks OR expensive powder from the USA.

We are an energy drink in the esports and gaming space. Our new product is an energy drink in powder in boxes of 30 sachets (please see attached for product example)

Please see example 1 and 2 for our competitors product. We would ideally like to go a bit more minimalist than them but still have a great color pop on black backing.

Target Market(s)

Gamer's and esports athletes between the ages or 18-30

Font styles to use
Sans Serif
Other font styles liked:
• Helvetica

Colors
886aae
ffffff

Requirements
Must have
• Black base/background.
• Vibrant purple N in the Velocity Logo.
• Same or slightly different shades of purple for some text and highlights.
• Black, white and some shades of a vibrant purple (for the grape flavor)
• ingredients list (may need to be reformatted to suit)
• Please see attached for legislative requirements on the box and sachets.
Nice to have
• minimalist design but enough to be eye catching and somewhat playful
• Twitter: @VLCT_FUEL
• Instagram: @VLCT_FUEL
• Facebook: @VLCTFUEL
Should not have
• OTHER COLORS.
• Overly complex designs.

```html
<!DOCTYPE html>
<html lang="en">
<head>
<meta charset="utf-8">
<title>Velocity Energy Drink – Grape Flavour Packaging</title>
<link href="https://fonts.googleapis.com/css2?family=Saira+Semi+Condensed:wght@400;500;600;700;800&display=swap" rel="stylesheet">
<style>
  :root {
    --stage: #e8e8eb;
    --black-top: #3d3d40;
    --black-bottom: #1b1b1d;
    --grape: #7d2a9e;
    --grape-deep: #55208a;
    --grape-bright: #a23ad0;
    --brand-lilac: #886aae;
    --white: #ffffff;
    --soft-white: #e6e6ea;
    --rule: #9a9aa0;
    --font: "Saira Semi Condensed", "Helvetica Neue", Arial, sans-serif;
  }
  * { box-sizing: border-box; margin: 0; padding: 0; }
  html, body { width: 1200px; height: 969px; overflow: hidden; }
  body { background: var(--stage); font-family: var(--font); color: var(--white); position: relative; }

  .panel {
    position: absolute; top: 40px; height: 560px; overflow: hidden;
    background: linear-gradient(180deg, var(--black-top) 0%, #2a2a2c 45%, var(--black-bottom) 100%);
  }
  .panel-front { left: 155px; width: 340px; }
  .panel-side { left: 515px; width: 130px; }
  .panel-back { left: 665px; width: 380px; }
  .panel svg.decor { position: absolute; inset: 0; }

  .wordmark { font-weight: 800; letter-spacing: 1px; color: var(--white); text-transform: uppercase; display: flex; align-items: center; gap: 8px; }
  .wordmark .mark-square { width: 0.42em; height: 0.42em; background: var(--grape-bright); }

  /* front */
  .serves-tab { position: absolute; left: 0; top: 0; width: 62px; height: 56px; background: linear-gradient(135deg, var(--grape-bright), var(--grape-deep)); clip-path: polygon(0 0, 100% 0, 70% 100%, 0 100%); padding: 6px 0 0 7px; line-height: 1; }
  .serves-tab .count { font-size: 24px; font-weight: 800; display: block; }
  .serves-tab .unit { font-size: 11px; font-weight: 700; }
  .panel-front .wordmark { position: absolute; top: 92px; width: 100%; justify-content: center; font-size: 40px; }
  .front-title { position: absolute; top: 378px; width: 100%; text-align: center; font-size: 30px; font-weight: 800; letter-spacing: 0.5px; }
  .tagline { position: absolute; top: 420px; width: 100%; text-align: center; font-size: 15px; font-style: italic; font-weight: 500; }
  .flavour-block { position: absolute; top: 464px; width: 100%; text-align: center; }
  .flavour-name { font-size: 22px; font-weight: 700; }
  .flavour-sub { font-size: 18px; font-weight: 500; margin-top: -2px; }
  .net-qty { font-size: 11px; font-weight: 500; margin-top: 6px; }

  /* side */
  .panel-side .wordmark { position: absolute; left: 50%; top: 280px; font-size: 34px; transform: translate(-50%, -50%) rotate(-90deg); white-space: nowrap; }

  /* back */
  .panel-back .wordmark { position: absolute; top: 26px; width: 100%; justify-content: center; font-size: 30px; }
  .back-title { position: absolute; top: 76px; width: 100%; text-align: center; font-size: 16px; font-weight: 700; line-height: 1.1; }
  .back-title span { display: block; font-size: 13px; font-weight: 500; }
  .back-copy { position: absolute; left: 30px; right: 30px; font-size: 8.5px; line-height: 1.3; }
  .back-copy b { font-weight: 700; }
  .directions { top: 120px; }
  .usage { top: 146px; }
  .nutrition { position: absolute; top: 164px; left: 34px; width: 312px; border-collapse: collapse; font-size: 7.5px; line-height: 1.15; text-transform: none; }
  .nutrition th, .nutrition td { border-bottom: 1px solid var(--rule); padding: 1px 3px; font-weight: 500; text-align: right; }
  .nutrition th:first-child, .nutrition td:first-child { text-align: left; border-right: 1px solid var(--rule); }
  .nutrition td:nth-child(2) { border-right: 1px solid var(--rule); }
  .nutrition .heading td { text-align: left; font-weight: 600; }
  .nutrition .sub td:first-child { padding-left: 12px; }
  .ingredients { top: 400px; font-size: 7.5px; text-align: justify; }
  .storage { top: 446px; text-align: center; font-weight: 600; font-size: 8.5px; }
  .best-before { top: 480px; display: flex; justify-content: space-between; font-size: 8.5px; }
  .back-band { position: absolute; left: 0; right: 0; bottom: 0; height: 46px; background: linear-gradient(90deg, var(--grape-deep), var(--grape)); padding: 5px 16px; display: flex; justify-content: space-between; font-size: 7.5px; line-height: 1.2; }
  .importer b { font-weight: 700; }
  .contact { text-align: right; align-self: center; }
  .web { font-size: 9px; margin-bottom: 3px; }
  .socials { display: flex; gap: 8px; }
  .social { display: flex; align-items: center; gap: 3px; }
  .social::before { content: ""; width: 7px; height: 7px; border-radius: 50%; background: var(--white); }

  /* sachet */
  .sachet { position: absolute; left: 180px; top: 660px; width: 840px; height: 230px; overflow: hidden; background: linear-gradient(180deg, #2e2e31, #141416); }
  .sachet svg.decor { position: absolute; inset: 0; }
  .crimp { position: absolute; top: 0; bottom: 0; width: 34px; background: repeating-linear-gradient(90deg, #222225 0 2px, #3a3a3e 2px 4px); }
  .crimp-left { left: 0; } .crimp-right { right: 0; }
  .sachet .wordmark { position: absolute; left: 70px; top: 36px; font-size: 38px; }
  .sachet-title { position: absolute; left: 540px; top: 38px; font-size: 28px; font-weight: 800; font-style: italic; }
  .sachet-tagline { position: absolute; left: 566px; top: 76px; font-size: 14px; font-style: italic; }
  .sachet-flavour { position: absolute; left: 540px; top: 128px; width: 250px; text-align: center; font-style: italic; }
  .sachet-flavour .flavour-name { font-size: 22px; }
  .sachet-flavour .flavour-sub { font-size: 17px; }
  .sachet-flavour .net-qty { font-size: 9px; font-weight: 600; margin-top: 2px; }
</style>
</head>
<body>

<!-- Front face -->
<section class="panel panel-front">
  <svg class="decor" viewBox="0 0 340 560" aria-hidden="true">
    <defs>
      <linearGradient id="frontBand" x1="0" y1="1" x2="1" y2="0">
        <stop offset="0" stop-color="#7d2a9e" stop-opacity="0.6"/>
        <stop offset="1" stop-color="#7d2a9e"/>
      </linearGradient>
      <linearGradient id="frontFoot" x1="0" y1="0" x2="1" y2="0">
        <stop offset="0" stop-color="#5a1f8a"/>
        <stop offset="1" stop-color="#7d2a9e"/>
      </linearGradient>
    </defs>
    <polygon points="20,420 340,150 340,230 110,420" fill="url(#frontBand)"/>
    <polygon points="0,480 60,480 95,452 245,452 280,480 340,480 340,560 0,560" fill="url(#frontFoot)"/>
  </svg>
  <div class="serves-tab"><span class="count">30</span><span class="unit">serves</span></div>
  <div class="wordmark"><span>Velocity</span><span class="mark-square"></span></div>
  <h1 class="front-title">ENERGY DRINK</h1>
  <p class="tagline">For gamers, By gamers</p>
  <div class="flavour-block">
    <p class="flavour-name">Grape flavour</p>
    <p class="flavour-sub">With Ginseng &amp; Caffeine</p>
    <p class="net-qty">Formulated Caffeinated Beverage&nbsp; 150 g (30 x 5 g)</p>
  </div>
</section>

<!-- Side face -->
<section class="panel panel-side">
  <svg class="decor" viewBox="0 0 130 560" aria-hidden="true">
    <polygon points="0,240 130,110 130,170 0,300" fill="#7d2a9e" opacity="0.85"/>
    <rect x="0" y="480" width="130" height="80" fill="#5a1f8a"/>
  </svg>
  <div class="wordmark"><span>Velocity</span><span class="mark-square"></span></div>
</section>

<!-- Back face -->
<section class="panel panel-back">
  <div class="wordmark"><span>Velocity</span><span class="mark-square"></span></div>
  <h2 class="back-title">Grape flavour Energy Drink<span>With Ginseng &amp; Caffeine</span></h2>
  <p class="back-copy directions"><b>Directions for Use:</b> Place one tablet in 400 ml water, stir until dissolved, and consume immediately.</p>
  <p class="back-copy usage"><b>Usage:</b> Maximum of two tablets per day</p>
  <table class="nutrition">
    <tr class="heading"><td colspan="3">NUTRITION INFORMATION</td></tr>
    <tr><td>SERVINGS PER PACKAGE:</td><td colspan="2" style="text-align:left">30</td></tr>
    <tr><td>SERVING SIZE:</td><td colspan="2" style="text-align:left">5g powder &amp; 500 ml water</td></tr>
    <tr><th></th><th>AV QUANTITY PER SERVING (400 ml)</th><th>AV QUANTITY PER 100 ml</th></tr>
    <tr><td>ENERGY</td><td>5 kJ</td><td>1 kJ</td></tr>
    <tr><td>PROTEIN</td><td>0.0 g</td><td>0.0 g</td></tr>
    <tr><td>FAT TOTAL</td><td>0.0 g</td><td>0.0 g</td></tr>
    <tr class="sub"><td>Saturated Fat</td><td>0.0 g</td><td>0.0 g</td></tr>
    <tr><td>CARBOHYDRATE</td><td>0.3 g</td><td>0.1 g</td></tr>
    <tr class="sub"><td>Sugars</td><td>0.0 g</td><td>0.0 g</td></tr>
    <tr><td>SODIUM</td><td>250 mg</td><td>62 mg</td></tr>
    <tr class="heading"><td colspan="3">Composition Information</td></tr>
    <tr><td>Caffeine</td><td>100 mg</td><td>25 mg</td></tr>
    <tr><td>Thiamin (B1)</td><td>10 mg</td><td>2.5 mg</td></tr>
    <tr><td>Riboflavin (B2)</td><td>5 mg</td><td>1.2 mg</td></tr>
    <tr><td>Niacin (B3)</td><td>20 mg</td><td>5 mg</td></tr>
    <tr><td>B6 (Pyridoxine)</td><td>5 mg</td><td>1.2 mg</td></tr>
    <tr><td>Taurine</td><td>500 mg</td><td>125 mg</td></tr>
    <tr><td>Inositol</td><td>50 mg</td><td>12.5 mg</td></tr>
  </table>
  <p class="back-copy ingredients">Acidity regulator (citric acid, sodium citrate), mineral salt (sodium bicarbonate), taurine, natural orange juice powder (8.5%) (maltodextrin, sugar, orange juice concentrate), caffeine (2.8%), inositol, vitamins (B3, B1, B6, B2), ginseng extract (0.5%), sweetener (steviol glycoside), mineral salt (magnesium stearate).</p>
  <p class="back-copy storage">Store in a cool dry place, away from sunlight below 25&deg;C.<br>Keep away from children</p>
  <p class="back-copy best-before"><span><b>Best Before:</b> See base of packaging</span><span>Made in China</span></p>
  <footer class="back-band">
    <div class="importer">Imported By:<br><b>Arcade Nutrition Pty Ltd</b><br>42 Harbour Lane<br>Geelong VIC 3220, Australia</div>
    <div class="contact">
      <p class="web">www.velocityfuel.shop</p>
      <div class="socials">
        <span class="social">@VLCT_FUEL</span>
        <span class="social">@VLCT_FUEL</span>
        <span class="social">@VLCTFUEL</span>
      </div>
    </div>
  </footer>
</section>

<!-- Sachet -->
<section class="sachet">
  <svg class="decor" viewBox="0 0 840 230" aria-hidden="true">
    <defs>
      <linearGradient id="sachetBand" x1="0" y1="1" x2="1" y2="0">
        <stop offset="0" stop-color="#55208a"/>
        <stop offset="1" stop-color="#8e2fb8"/>
      </linearGradient>
      <linearGradient id="sachetFoot" x1="0" y1="0" x2="1" y2="0">
        <stop offset="0" stop-color="#7d2a9e"/>
        <stop offset="1" stop-color="#a23ad0"/>
      </linearGradient>
    </defs>
    <polygon points="300,230 560,0 660,0 400,230" fill="url(#sachetBand)" opacity="0.9"/>
    <polygon points="520,120 806,120 806,230 470,230" fill="url(#sachetFoot)"/>
  </svg>
  <div class="crimp crimp-left"></div>
  <div class="crimp crimp-right"></div>
  <div class="wordmark"><span>Velocity</span><span class="mark-square"></span></div>
  <p class="sachet-title">ENERGY DRINK</p>
  <p class="sachet-tagline">For gamers, By gamers</p>
  <div class="sachet-flavour">
    <p class="flavour-name">Grape flavour</p>
    <p class="flavour-sub">With Ginseng &amp; Caffeine</p>
    <p class="net-qty">Formulated Caffeinated Beverage 5g</p>
  </div>
</section>

</body>
</html>
```